website for LanternPeak Advisory - a HR Consultancy Company

Creation of a website template. I would like to make it with with Wix, but am open to other online website programms.

Website is for consulting company in human resources offering the following services:
- Human resources and talent management for small companies
- Human resources consulting for start-ups
- Diversity and Inclusion management/training
- Board of Directors - talent identification and need evalutation
- coaching and counseling

Pages needed:
- Home page
- HR and talent management
- HR consulting for start-ups
- Diversity & Inclusion management/training
- coaching and counseling
- contact

1. My logo below
2. an example website that I like (not in terms of colours): https://www.mapleridgeadvisors.ch/
http://www.veldorquint.ch/

Target Market(s)

small and mid-sized companies, start-ups

Industry/Entity Type

Consulting

Number of Pages Required

5+ page

Font styles to use
Serif
Sans Serif

Colors
3277b5
35a7d7

Requirements
Must have
• - easy on the eye yet professional looking
• - my text is short
• - website should be clear and easy to understand
Nice to have
• - I will include photographs of the coaches
Should not have
• too many colours
• complicated

```html
<!DOCTYPE html>
<html lang="en">
<head>
<meta charset="utf-8">
<title>LanternPeak Advisory — Home</title>
<link rel="stylesheet" href="https://fonts.googleapis.com/css2?family=Montserrat:wght@400;500;700;800&family=Crimson+Text:wght@400&display=swap">
<style>
  :root {
    --brand-blue: #2472b6;
    --brand-sky: #35a7d7;
    --header-grey: #eeeeee;
    --ink: #1c1c1c;
    --white: #ffffff;
    --field-grey: #efefef;
    --field-text: #cfcfcf;
    --sans: "Montserrat", Arial, sans-serif;
    --serif: "Crimson Text", Georgia, serif;
  }
  * { margin: 0; padding: 0; box-sizing: border-box; }
  html, body { width: 927px; height: 1200px; overflow: hidden; background: var(--white); }
  .page { position: relative; width: 927px; height: 1200px; font-family: var(--sans); color: var(--ink); }

  /* Header */
  .site-header { position: absolute; left: 0; top: 0; width: 927px; height: 152px; background: var(--header-grey); }
  .brand { position: absolute; left: 0; width: 927px; top: 58px; display: flex; justify-content: center; align-items: center; gap: 10px; }
  .brand-dot { width: 26px; height: 26px; border-radius: 50%; background: var(--brand-blue); }
  .brand-name { font-weight: 700; font-size: 22px; color: var(--brand-blue); letter-spacing: 0.5px; }

  /* Navigation */
  .main-nav { position: absolute; left: 0; top: 152px; width: 927px; height: 68px; background: var(--brand-blue); }
  .nav-tab { position: absolute; left: 394px; top: 0; width: 131px; height: 68px; background: var(--header-grey); clip-path: polygon(0 0, 100% 0, 79% 100%, 21% 100%); }
  .nav-link { position: absolute; top: 26px; font-weight: 700; font-size: 15px; color: var(--white); text-decoration: none; }
  .nav-link.is-active { color: var(--brand-blue); top: 23px; }

  /* Hero */
  .hero { position: absolute; left: 0; top: 220px; width: 927px; height: 485px;
    background: radial-gradient(ellipse at 30% 55%, #7fa89a 0%, #9bb9bd 35%, #a9c4d6 70%, #b6cfe0 100%); }
  .hero-quote { position: absolute; left: 505px; top: 175px; width: 335px; height: 102px; }
  .hero-quote svg { position: absolute; inset: 0; }
  .quote-line { position: absolute; font-family: var(--serif); font-size: 23px; color: var(--white); white-space: nowrap; }
  .quote-line.first { left: 10px; top: 18px; }
  .quote-line.second { right: 10px; top: 45px; }
  .hero-button { position: absolute; left: 565px; top: 294px; width: 210px; height: 32px; background: var(--white); border-radius: 3px;
    display: flex; align-items: center; justify-content: center; gap: 18px; font-weight: 700; font-size: 15px; color: var(--brand-blue); }
  .hero-dots { position: absolute; left: 427px; top: 445px; display: flex; gap: 14px; }
  .hero-dots span { width: 15px; height: 15px; border-radius: 50%; background: rgba(255,255,255,0.55); }
  .hero-dots span.is-current { background: var(--white); }

  /* News strip */
  .news { position: absolute; left: 0; top: 705px; width: 927px; height: 185px; background: var(--brand-blue); }
  .news-item { position: absolute; top: 19px; height: 144px; }
  .news-text { position: absolute; right: 141px; top: 0; width: 150px; text-align: right; color: var(--white); }
  .news-date { font-weight: 700; font-size: 16px; margin-bottom: 8px; white-space: nowrap; }
  .news-body { font-size: 11.5px; line-height: 14.5px; }
  .news-body strong { font-weight: 700; }
  .news-rule { position: absolute; right: 130px; top: 0; width: 2px; height: 144px; background: var(--white); }
  .news-photo { position: absolute; right: 0; top: 0; width: 120px; height: 144px; }

  /* Meeting signup */
  .signup { position: absolute; left: 0; top: 890px; width: 927px; height: 248px; }
  .signup-photo { position: absolute; right: 0; top: 0; width: 372px; height: 248px;
    clip-path: polygon(28% 0, 100% 0, 100% 100%, 0 100%);
    background: linear-gradient(100deg, rgba(255,255,255,1) 0%, #e9e4de 35%, #d8ccc0 70%, #cfd6dc 100%); }
  .signup-heading { position: absolute; left: 49px; top: 42px; font-weight: 700; font-size: 15px; }
  .signup-copy { position: absolute; left: 0; width: 606px; text-align: center; font-size: 15.5px; line-height: 18px; }
  .signup-copy.intro { top: 80px; }
  .signup-copy.note { top: 180px; }
  .email-field { position: absolute; left: 109px; top: 125px; width: 388px; height: 39px; background: var(--field-grey); border-radius: 4px;
    display: flex; align-items: center; justify-content: center; font-weight: 700; font-size: 17px; color: var(--field-text); }

  /* Footer */
  .site-footer { position: absolute; left: 0; top: 1138px; width: 927px; height: 62px; background: var(--brand-blue); color: var(--white); }
  .copyright { position: absolute; left: 20px; top: 23px; font-size: 13.5px; }
  .footer-brand { position: absolute; left: 0; width: 927px; top: 22px; text-align: center; font-weight: 700; font-size: 14px; }
  .footer-social { position: absolute; right: 21px; top: 17px; display: flex; gap: 11px; }
  .social-icon { width: 28px; height: 28px; border-radius: 50%; background: var(--white); display: flex; align-items: center; justify-content: center; }
</style>
</head>
<body>
<div class="page">

  <header class="site-header">
    <div class="brand">
      <span class="brand-dot"></span>
      <span class="brand-name">LanternPeak Advisory</span>
    </div>
  </header>

  <nav class="main-nav">
    <div class="nav-tab"></div>
    <a class="nav-link" style="left:95px">TALENT</a>
    <a class="nav-link" style="left:228px">CONSULTANCY</a>
    <a class="nav-link is-active" style="left:436px">HOME</a>
    <a class="nav-link" style="left:582px">TRAINING</a>
    <a class="nav-link" style="left:745px">DIRECTORS</a>
  </nav>

  <section class="hero" role="img" aria-label="Photo of lily pads floating on calm blue water">
    <div class="hero-quote">
      <svg width="335" height="102" viewBox="0 0 335 102" fill="none" stroke="#ffffff" stroke-width="2.5">
        <path d="M1 26 V1 H334 V45"/>
        <path d="M1 58 V101 H334 V85"/>
      </svg>
      <span class="quote-line first">The Willingness to Learn is the</span>
      <span class="quote-line second">Acknowledgment of Trust</span>
    </div>
    <div class="hero-button">
      <span>Do You Trust Us?</span>
      <svg width="7" height="10" viewBox="0 0 7 10"><path d="M0 0 L7 5 L0 10 Z" fill="#2472b6"/></svg>
    </div>
    <div class="hero-dots"><span class="is-current"></span><span></span><span></span></div>
  </section>

  <section class="news">
    <article class="news-item" style="left:0; width:311px">
      <div class="news-text">
        <div class="news-date">SEPTEMBER 12</div>
        <p class="news-body">See how we could help you with your next human sources meeting with Dr. Hollis of Brenwick Labs. <strong>Click Me!</strong></p>
      </div>
      <div class="news-rule"></div>
      <div class="news-photo" role="img" aria-label="Portrait photo of a smiling woman" style="background:linear-gradient(160deg,#b88a4a,#d9b98a 60%,#efe6d8)"></div>
    </article>
    <article class="news-item" style="left:290px; width:311px">
      <div class="news-text">
        <div class="news-date">SEPTEMBER 04</div>
        <p class="news-body">Last week we mad a great discovery on how the market is affected by the consumer with the lowest budget. <strong>Click Here!</strong></p>
      </div>
      <div class="news-rule"></div>
      <div class="news-photo" role="img" aria-label="Photo of hands working over papers on a desk" style="background:linear-gradient(150deg,#8a6a3e,#c9b38c 55%,#e6e0d2)"></div>
    </article>
    <article class="news-item" style="left:581px; width:311px">
      <div class="news-text">
        <div class="news-date">AUGUST 29</div>
        <p class="news-body">Believe it or not, but consumer stats and analytics goes a very long way with marketers and accountants. <strong>See How!</strong></p>
      </div>
      <div class="news-rule"></div>
      <div class="news-photo" role="img" aria-label="Photo of two colleagues looking at a screen together" style="background:linear-gradient(150deg,#5a4632,#a98c6a 55%,#d8cdb8)"></div>
    </article>
  </section>

  <section class="signup">
    <div class="signup-photo" role="img" aria-label="Faded photo of a presenter speaking to a meeting group"></div>
    <h2 class="signup-heading">SCHEDULE YOUR NEXT MEETING WITH OUR RESOURCE DIRECTORS!</h2>
    <p class="signup-copy intro">Would you like to meet with our resource specialists in your area?<br>Add yourself to our consultation list so that we may contact you!</p>
    <div class="email-field">PLACE YOUR E-MAIL HERE</div>
    <p class="signup-copy note">After adding yourself, we will send you a confirmation field<br>for you to sign yourself up for our next meeting location.</p>
  </section>

  <footer class="site-footer">
    <div class="copyright">Copyright: LanternPeak Advisory | 2017</div>
    <div class="footer-brand">LanternPeak Advisory</div>
    <div class="footer-social">
      <span class="social-icon" aria-label="Social network link"></span>
      <span class="social-icon" aria-label="Social network link"></span>
      <span class="social-icon" aria-label="Social network link"></span>
      <span class="social-icon" aria-label="Email">
        <svg width="16" height="12" viewBox="0 0 16 12"><rect x="0.5" y="0.5" width="15" height="11" rx="2" fill="#2472b6"/><path d="M1 2 L8 7 L15 2" stroke="#ffffff" stroke-width="1.5" fill="none"/></svg>
      </span>
      <span class="social-icon" aria-label="Location">
        <svg width="12" height="17" viewBox="0 0 12 17"><path d="M6 0 C2.7 0 0 2.6 0 5.9 C0 10 6 17 6 17 C6 17 12 10 12 5.9 C12 2.6 9.3 0 6 0 Z" fill="#2472b6"/><circle cx="6" cy="6" r="2.3" fill="#ffffff"/></svg>
      </span>
    </div>
  </footer>

</div>
</body>
</html>
```